Banner signature

Hi, looking for a banner for email signature 728 px wide and 200 px high
Could we have our 10 year logo and premium logo, a similar look and feel of our previous banner design (I've attached) and also include an aboriginal design with the Wording
This email comes to you from Gubbi Gubbi country
I've attached an example of some look and feels that we like.
Can we have the background of banner the Blue colour of our Fern & Tide logo and

```html
<!DOCTYPE html>
<html lang="en">
<head>
<meta charset="utf-8">
<title>Email Signature Banner</title>
<link rel="stylesheet" href="https://fonts.googleapis.com/css2?family=Kalam:wght@700&family=Play:wght@700&display=swap">
<style>
  :root {
    --page-blue: #29bbff;
    --banner-white: #ffffff;
    --navy: #0d4f91;
    --navy-deep: #0b4585;
    --navy-light: #1a6fb8;
    --sky: #36b8f5;
    --ribbon-dark: #0f5fa8;
    --gold: #d6b04a;
    --motif-blue: #8fd3f5;
    --motif-sand: #d9c3a5;
    --text-light: #ffffff;
  }
  html, body {
    margin: 0;
    padding: 0;
    width: 1200px;
    height: 1200px;
    overflow: hidden;
    background: var(--page-blue);
  }
  .canvas {
    position: relative;
    width: 1200px;
    height: 1200px;
  }
  .signature-banner {
    position: absolute;
    left: 163.2px;
    top: 480px;
    width: 873.6px;
    height: 240px;
    box-shadow: 0 18px 40px rgba(0, 60, 120, 0.25);
  }
  .signature-banner svg { display: block; width: 100%; height: 100%; }
  .lead-line { font-family: "Kalam", cursive; font-weight: 700; font-size: 19px; fill: var(--text-light); }
  .country-name { font-family: "Play", sans-serif; font-weight: 700; font-size: 51px; fill: var(--text-light); letter-spacing: 1.5px; }
  .country-word { font-family: "Kalam", cursive; font-weight: 700; font-size: 23px; fill: var(--text-light); }
  .brand-name { font-family: "Play", sans-serif; font-weight: 700; font-size: 11px; fill: var(--navy); }
</style>
</head>
<body>
<div class="canvas">
  <div class="signature-banner">
    <svg viewBox="0 0 728 200" xmlns="http://www.w3.org/2000/svg">
      <defs>
        <linearGradient id="navyPanel" x1="0" y1="0" x2="1" y2="1">
          <stop offset="0" stop-color="var(--navy-deep)"/>
          <stop offset="0.6" stop-color="var(--navy)"/>
          <stop offset="1" stop-color="var(--navy-light)"/>
        </linearGradient>
        <radialGradient id="motifSky">
          <stop offset="0" stop-color="var(--sky)" stop-opacity="0.55"/>
          <stop offset="1" stop-color="var(--sky)" stop-opacity="0"/>
        </radialGradient>
        <radialGradient id="motifPale">
          <stop offset="0" stop-color="var(--motif-blue)" stop-opacity="0.5"/>
          <stop offset="1" stop-color="var(--motif-blue)" stop-opacity="0"/>
        </radialGradient>
        <radialGradient id="motifSand">
          <stop offset="0" stop-color="var(--motif-sand)" stop-opacity="0.6"/>
          <stop offset="1" stop-color="var(--motif-sand)" stop-opacity="0"/>
        </radialGradient>
      </defs>

      <rect class="banner-base" width="728" height="200" fill="var(--banner-white)"/>

      <g class="accent-stripes" fill="var(--sky)">
        <polygon points="282,0 288,0 222,200 216,200"/>
        <polygon points="296,0 304,0 238,200 230,200"/>
        <polygon points="310,0 314,0 248,200 244,200"/>
      </g>

      <polygon class="navy-panel" points="319,0 728,0 728,200 259,200" fill="url(#navyPanel)"/>

      <g class="motif-spots">
        <circle role="img" aria-label="Aboriginal concentric circle motif" cx="16" cy="18" r="24" fill="url(#motifSand)"/>
        <circle role="img" aria-label="Aboriginal concentric circle motif" cx="186" cy="64" r="22" fill="url(#motifPale)"/>
        <circle role="img" aria-label="Aboriginal concentric circle motif" cx="64" cy="192" r="24" fill="url(#motifPale)"/>
        <circle role="img" aria-label="Aboriginal concentric circle motif" cx="382" cy="8" r="26" fill="url(#motifSky)"/>
        <circle role="img" aria-label="Aboriginal concentric circle motif" cx="700" cy="18" r="26" fill="url(#motifSand)"/>
        <circle role="img" aria-label="Aboriginal concentric circle motif" cx="350" cy="198" r="24" fill="url(#motifSky)"/>
        <circle role="img" aria-label="Aboriginal concentric circle motif" cx="624" cy="180" r="26" fill="url(#motifSky)"/>
        <circle role="img" aria-label="Aboriginal concentric circle motif" cx="470" cy="118" r="22" fill="url(#motifSky)" opacity="0.6"/>
      </g>

      <g class="premium-ribbon">
        <polygon points="54,0 112,0 112,135 83,112 54,135" fill="var(--sky)"/>
        <polygon points="92,112 112,112 112,135" fill="var(--ribbon-dark)"/>
        <circle cx="83" cy="60" r="40" fill="var(--banner-white)"/>
        <text class="brand-name" x="83" y="64" text-anchor="middle">Fern &amp; Tide</text>
      </g>

      <circle class="anniversary-badge" role="img" aria-label="10 year anniversary badge" cx="250" cy="102" r="62" fill="var(--gold)"/>

      <text class="lead-line" x="392" y="66">This email comes to you from</text>
      <text class="country-name" x="388" y="118">Gubbi Gubbi</text>
      <text class="country-word" x="391" y="148">country</text>
    </svg>
  </div>
</div>
</body>
</html>
```